Vemtra Group: Business Card for a high end technology company

We need a cool new design for our business cards using our cloud logo. We are a technology consulting business. We pride ourselves on be the best of the best. We mainly focus on cloud solutions and managed services. We need a business card that sets us apart from the other technology companies in the area and allows us to stand out.

Target Market(s)

Technology departments, CIO, CEOs, and Information Technology Staff.

Industry/Entity Type

Information Technology

Contact Information for Business Card

Must have the logo and our name.
Must have employee name, email address, office phone, cell phone and website.
Need to have all info on one side a cool design on backside.

Font styles to use
Serif
Sans Serif

Requirements
Must have
• Must have the logo and our name.
• Must have employee name, email address, office phone, cell phone and website.
• Need to have all info on one side a cool design on back side.
• Must be a crisp clean design, not too busy or confusing.

```html
<!DOCTYPE html>
<html lang="en">
<head>
<meta charset="utf-8">
<title>Vemtra Group – Stationery</title>
<link rel="stylesheet" href="https://fonts.googleapis.com/css2?family=Roboto:wght@400&display=swap">
<style>
  :root {
    --backdrop: #2a2a2a;
    --paper: #ffffff;
    --brand-blue: #00a2df;
    --rule-blue: #5cc8ee;
    --ink: #2e2e2e;
    --ink-soft: #3a3a3a;
  }
  html, body {
    margin: 0;
    padding: 0;
    overflow: hidden;
  }
  body {
    width: 1200px;
    height: 1010px;
    background: var(--backdrop);
    font-family: "Roboto", Arial, sans-serif;
    color: var(--ink);
    position: relative;
  }
  .letterhead {
    position: absolute;
    left: 170px;
    top: 140px;
    width: 510px;
    height: 722px;
    background: var(--paper);
  }
  .brand {
    display: flex;
    align-items: center;
    gap: 8px;
    font-size: 15px;
    color: var(--ink-soft);
    letter-spacing: 0.2px;
  }
  .brand-dot {
    width: 12px;
    height: 12px;
    border-radius: 50%;
    background: var(--brand-blue);
  }
  .letterhead .brand {
    position: absolute;
    left: 38px;
    top: 58px;
  }
  .letterhead-rule {
    position: absolute;
    left: 92px;
    right: 38px;
    top: 630px;
    height: 1px;
    background: var(--rule-blue);
  }
  .letterhead-contact {
    position: absolute;
    left: 92px;
    top: 640px;
    font-size: 9px;
    line-height: 12px;
    color: var(--ink);
  }
  .card {
    position: absolute;
    left: 790px;
    width: 220px;
    height: 140px;
  }
  .card-front {
    top: 380px;
    background: var(--brand-blue);
    color: var(--ink);
    text-align: center;
    font-size: 9px;
  }
  .card-front .employee {
    position: absolute;
    top: 48px;
    left: 0;
    right: 0;
  }
  .card-front .contact {
    position: absolute;
    top: 84px;
    left: 0;
    right: 0;
    line-height: 12px;
  }
  .card-back {
    top: 528px;
    background: var(--paper);
    display: flex;
    align-items: center;
    justify-content: center;
  }
  .card-back .brand {
    font-size: 14px;
  }
</style>
</head>
<body>
  <section class="letterhead">
    <div class="brand"><span class="brand-dot"></span><span>Vemtra Group</span></div>
    <div class="letterhead-rule"></div>
    <div class="letterhead-contact">
      email address<br>
      office phone<br>
      cell phone<br>
      www.vemtragroup.com
    </div>
  </section>

  <section class="card card-front">
    <div class="employee">employee name</div>
    <div class="contact">
      email address<br>
      office phone<br>
      cell phone<br>
      www.vemtragroup.com
    </div>
  </section>

  <section class="card card-back">
    <div class="brand"><span class="brand-dot"></span><span>Vemtra Group</span></div>
  </section>
</body>
</html>
```